Harbor Nightclub

Nightclub flyer., digital single sided, for KV and PX. I included samples of some previous flyers we've used. Sample Info:
HARBOR
FRIDAYS
FRI MAY 1 2020
DJ VORTAN (club floor)
DJ RUZO & DJ TAV (residents on the lounge floor)
4217 Marlow Avenue Sacramento
www.harborvenuehall.example for list/VIP inquiries

Target Market(s)

Upscale top 40 crowd but want some cool and artsy like the examples included.

Font styles to use
Sans Serif

Requirements
Must have
• Harbor Logo
Nice to have
• Would be nice if the flyer can be incorporated later with DJ photos (sometimes we will add dj photos to pixagram etc). Would like a big city type of feel.
Should not have
• Nothing too sexual.

```html
<!DOCTYPE html>
<html lang="en">
<head>
<meta charset="utf-8">
<title>Harbor Fridays Flyer</title>
<link rel="stylesheet" href="https://fonts.googleapis.com/css2?family=Jost:wght@300;400;600;700&display=swap">
<style>
  :root {
    --stage: #6c6e70;
    --ink: #050307;
    --white: #ffffff;
    --neon: #b84dff;
    --neon-soft: rgba(190, 80, 255, 0.55);
    --violet: #6f2bc9;
    --violet-deep: #3a1477;
    --grey-text: #c9c9cf;
    --url: #a05ac8;
  }
  * { box-sizing: border-box; margin: 0; padding: 0; }
  html, body {
    width: 1200px;
    height: 1200px;
    overflow: hidden;
    background: var(--stage);
    font-family: "Jost", sans-serif;
  }
  .flyer {
    position: absolute;
    left: 255px;
    top: 141px;
    width: 690px;
    height: 918px;
    background: var(--ink);
    overflow: hidden;
  }
  .alley-photo {
    position: absolute;
    left: 0;
    top: 0;
    width: 690px;
    height: 660px;
    background:
      radial-gradient(ellipse 34% 52% at 48% 62%, rgba(150, 70, 230, 0.85), rgba(100, 40, 190, 0.55) 45%, transparent 75%),
      radial-gradient(ellipse 22% 20% at 50% 12%, rgba(120, 40, 120, 0.6), transparent 80%),
      radial-gradient(ellipse 10% 25% at 80% 22%, rgba(150, 30, 60, 0.35), transparent 80%),
      var(--ink);
  }
  .lasers {
    position: absolute;
    inset: 0;
    width: 690px;
    height: 918px;
  }
  .line {
    position: absolute;
    left: 0;
    width: 100%;
    text-align: center;
    transform: translateY(-50%);
    color: var(--white);
    white-space: nowrap;
  }
  .brand {
    top: 90px;
    display: flex;
    justify-content: center;
    align-items: center;
    gap: 12px;
    font-size: 31px;
    font-weight: 400;
    letter-spacing: 0.04em;
  }
  .brand-dot {
    width: 24px;
    height: 24px;
    border-radius: 50%;
    background: var(--white);
  }
  .night-title {
    top: 200px;
    font-size: 108px;
    font-weight: 400;
    letter-spacing: 0.01em;
    text-shadow: 0 0 6px var(--neon), 0 0 16px var(--neon), 0 0 30px var(--neon-soft);
  }
  .event-date {
    top: 307px;
    font-size: 29px;
    font-weight: 300;
    letter-spacing: 0.05em;
  }
  .headliner {
    top: 684px;
    font-size: 62px;
    font-weight: 700;
    letter-spacing: 0.04em;
  }
  .residents {
    top: 757px;
    display: flex;
    justify-content: center;
    align-items: center;
    gap: 24px;
    font-size: 32px;
    font-weight: 700;
    letter-spacing: 0.04em;
  }
  .residents-divider {
    width: 3px;
    height: 44px;
    background: var(--violet);
  }
  .venue-address {
    top: 844px;
    font-size: 19px;
    font-weight: 400;
    letter-spacing: 0.32em;
    color: var(--grey-text);
  }
  .venue-url {
    top: 883px;
    font-size: 13.5px;
    font-weight: 400;
    letter-spacing: 0.04em;
    color: var(--url);
  }
</style>
</head>
<body>
  <main class="flyer">
    <div class="alley-photo" role="img" aria-label="Night photo of a narrow cobblestone alley lit in purple and violet tones"></div>

    <svg class="lasers" viewBox="0 0 690 918" aria-hidden="true">
      <g stroke="#d27bff" stroke-linecap="round">
        <line x1="0" y1="228" x2="690" y2="755" stroke-width="6" opacity="0.25"/>
        <line x1="0" y1="228" x2="690" y2="755" stroke-width="1.5" opacity="0.9"/>
        <line x1="0" y1="610" x2="690" y2="388" stroke-width="6" opacity="0.25"/>
        <line x1="0" y1="610" x2="690" y2="388" stroke-width="1.5" opacity="0.9"/>
        <line x1="0" y1="250" x2="110" y2="205" stroke-width="4" opacity="0.2"/>
        <line x1="0" y1="250" x2="110" y2="205" stroke-width="1" opacity="0.7"/>
      </g>
    </svg>

    <div class="line brand"><span class="brand-dot"></span><span class="brand-name">HARBOR</span></div>
    <h1 class="line night-title">FRIDAYS</h1>
    <p class="line event-date">FRI MAY 1 2020</p>

    <h2 class="line headliner">DJ VORTAN</h2>
    <p class="line residents"><span>DJ RUZO</span><span class="residents-divider"></span><span>DJ TAV</span></p>

    <p class="line venue-address">4217 MARLOW AVENUE SACRAMENTO</p>
    <p class="line venue-url">www.harborvenuehall.example for list/VIP inquiries</p>
  </main>
</body>
</html>
```